Last Minute Accommodation Booking Portal

AlpenGlowDeals.com needs a web platform to put potential clients in touch with available local ski resort accommodation. We are a dynamic, friendly and versatile company; we like a clean, graphic, contemporary look!

Hotel and apartment owners offer rooms to rent for certain dates with pricing; clients can ask for specific dates and number of beds with their budget. Offers can see searchers requests, searchers can only see offers.

All dates requested and offered must be within two weeks of the posting date and then posts should be removed when their arrival date has passed or they can be deleted by the person posting. We are envisaging that the hotels/apartments and customers would each need to register and login their offer/request.

Target Market(s)

28-55 years, active, high net worth but like a bargain, last mintue deciders, skiers and snowboarders or mountain enthusiasts, city folk wanting a winter break

Industry/Entity Type

Accommodation

Coding

Number of Pages Required

Font styles to use
Sans Serif

Colors
cee9f5
33a6d7
e34297
b768aa
ffffff

Requirements
Must have
• Efficient functionality so that many different parties - both offering deals and searching for deals - can search/list at the same time.
• option to translate to french
Nice to have
• opt in to 'alert/notification' when new offer or search is listed

```html
<!DOCTYPE html>
<html lang="en">
<head>
<meta charset="utf-8">
<title>AlpenGlowDeals.com – Last Minute Accommodation</title>
<link rel="stylesheet" href="https://fonts.googleapis.com/css2?family=Lato:wght@400;700;900&family=Cormorant+Garamond:wght@500&display=swap">
<style>
:root{
  --sky:#cee9f5;
  --blue:#33a6d7;
  --pink:#e34297;
  --purple:#b768aa;
  --white:#ffffff;
  --ink:#3a3a3a;
  --muted:#8a8a8a;
  --line:#d8d8d8;
  --grey-tab:#9a9a9a;
  --footer:#4a4a4a;
  --footer-dark:#2f2f2f;
  --footer-mid:#8c8c8c;
}
*{box-sizing:border-box;margin:0;padding:0}
html,body{width:699px;height:1200px;overflow:hidden}
body{font-family:"Lato",Arial,sans-serif;color:var(--ink);background:var(--white);font-size:9px;position:relative}

/* Header */
.site-header{height:60px;display:flex;align-items:center;justify-content:space-between;padding:0 40px 0 38px}
.brand{font-weight:900;font-size:21px;color:var(--pink);letter-spacing:-.2px}
.main-nav{display:flex;font-size:8px;font-weight:700;letter-spacing:.6px;color:#666}
.main-nav a{padding:3px 8px;border-left:1px solid #bbb;color:inherit;text-decoration:none}
.main-nav a:first-child{border-left:none;border-bottom:2px solid var(--blue);color:var(--ink)}

/* Hero */
.hero{position:relative;height:290px;background:linear-gradient(180deg,#6f8fb5 0%,#b9c9da 30%,#e8eef3 55%,#cfd6de 70%,#9aa3a8 100%)}
.hero-title{position:absolute;left:0;right:0;bottom:14px;text-align:center;font-family:"Cormorant Garamond",Georgia,serif;font-size:24px;color:var(--white);letter-spacing:1.5px;text-shadow:0 1px 3px rgba(0,0,0,.5)}

/* Mode tabs */
.mode-tabs{display:flex;justify-content:center;gap:70px;margin-top:16px;font-size:12px;letter-spacing:.5px}
.mode-tabs span{padding:0 8px 5px;color:#666}
.mode-tabs .active{color:var(--blue);border-bottom:2px solid var(--blue)}

/* Search panel */
.search-panel{width:540px;margin:12px auto 0;background:var(--white);border:1px solid var(--line);box-shadow:0 2px 6px rgba(0,0,0,.18);padding:10px 12px 12px}
.type-tabs{display:flex;gap:4px;margin-bottom:8px}
.type-tabs span{flex:1;height:16px;color:var(--white);font-size:7px;font-weight:700;background:var(--grey-tab);display:flex;align-items:center;justify-content:center;gap:4px}
.type-tabs .active{background:var(--blue)}
.search-form{display:grid;grid-template-columns:1fr 1fr 1fr;gap:6px 8px}
.field{height:17px;border:1px solid var(--line);font-size:6.5px;color:var(--muted);padding:0 5px;display:flex;align-items:center;justify-content:space-between}
.field-notes{grid-column:3;grid-row:1 / span 2;height:40px;align-items:flex-start;padding-top:4px}
.form-actions{grid-column:3;display:flex;gap:5px}
.btn{display:inline-flex;align-items:center;justify-content:center;height:17px;color:var(--white);font-size:7px;font-weight:700;letter-spacing:.4px;padding:0 10px;border:none}
.btn-blue{background:var(--blue)}
.btn-purple{background:var(--purple)}
.btn-dark{background:#555}

/* Welcome */
.welcome{text-align:center;padding:26px 90px 0}
.welcome h1{font-size:18px;font-weight:700;color:var(--purple)}
.welcome h1 strong{color:var(--pink);font-weight:900}
.divider{width:150px;height:1px;background:var(--line);margin:8px auto 12px;position:relative}
.divider::after{content:"";position:absolute;left:71px;top:-3px;width:7px;height:7px;border-radius:50%;background:var(--blue)}
.welcome p{font-size:6.5px;line-height:1.6;color:#666;margin-bottom:8px}
.welcome .btn{margin-top:6px;height:18px;padding:0 16px;border-radius:2px}

/* Listings */
.listings{position:absolute;top:727px;left:0;width:699px;height:285px;background:var(--blue);padding:14px 30px 0}
.listings-head{display:flex;justify-content:space-between;align-items:flex-end;color:var(--white);border-bottom:1px solid rgba(255,255,255,.6);padding-bottom:4px;margin-bottom:10px}
.listings-head h2{font-size:14px;font-weight:900;letter-spacing:.3px}
.listings-head a{font-size:7px;color:var(--white);text-decoration:underline}
.listing{display:flex;background:var(--white);height:68px;margin-bottom:6px;padding:5px 6px;gap:8px;overflow:hidden}
.listing-photo{width:58px;height:40px;background:linear-gradient(160deg,#b9c6d2,#7f6a58 70%,#eef2f5)}
.listing-main{width:60px;display:flex;flex-direction:column;gap:4px}
.listing-main .btn{height:13px;font-size:6px;padding:0;width:58px}
.listing-body{flex:1;display:flex;flex-direction:column;min-width:0}
.listing-top{display:flex;justify-content:space-between}
.listing-title{font-size:7px;font-weight:700;color:var(--ink)}
.listing-actions{display:flex;gap:12px;font-size:6.5px;font-weight:900;color:#555}
.listing-actions span{display:flex;align-items:center;gap:3px}
.listing-desc{font-size:5.6px;line-height:1.5;color:#777;margin-top:3px}
.listing-meta{display:flex;gap:12px;margin-top:auto;font-size:5.8px;color:#555;align-items:center}
.listing-meta b{font-weight:700}
.listing-meta .tag{display:flex;align-items:center;gap:3px;font-weight:700}

/* Footer */
.site-footer{position:absolute;top:1012px;left:0;width:699px;height:160px;background:var(--footer);display:grid;grid-template-columns:1fr 1fr 1fr;color:var(--white)}
.footer-col{padding:12px 30px}
.footer-col h3{font-size:9px;font-weight:700;margin-bottom:10px}
.login-field{height:13px;background:var(--white);color:#777;font-size:6.5px;padding:0 4px;display:flex;align-items:center;margin-bottom:6px;width:110px}
.login .btn{height:13px;font-size:6.5px;padding:0 10px}
.social{display:flex;gap:4px;margin-top:8px}
.social span{width:10px;height:10px;background:var(--blue)}
.social span:nth-child(2){background:#4aa8e0}
.social span:nth-child(3){background:#d9453a}
.social span:nth-child(4){background:#c33b7d}
.testimonials{background:var(--footer-mid);margin-top:-6px;box-shadow:0 0 8px rgba(0,0,0,.3)}
.testimonials h3{text-align:center;font-size:10px}
.quote-card{background:var(--white);color:#666;font-size:6px;line-height:1.5;padding:7px 8px;position:relative}
.quote-card::after{content:"";position:absolute;left:14px;bottom:-6px;border:6px solid transparent;border-top-color:var(--white);border-bottom:0}
.quote-author{font-size:6px;margin:10px 0 0 30px}
.newsletter{display:flex;flex-direction:column}
.newsletter-box{background:var(--footer-dark);padding:8px;font-size:6px;line-height:1.5;color:#ddd}
.signup{display:flex;margin-top:7px}
.signup .field{background:var(--white);flex:1;height:12px;font-size:6px;border:none}
.signup .btn{height:12px;width:14px;padding:0}
.copyright{position:absolute;top:1172px;left:0;width:699px;height:28px;background:var(--blue);color:var(--white);font-size:6.5px;text-align:center;line-height:28px}
</style>
</head>
<body>

<header class="site-header">
  <div class="brand">AlpenGlowDeals</div>
  <nav class="main-nav"><a href="#">HOME</a><a href="#">OFFERS</a><a href="#">ABOUT</a><a href="#">NEWS</a></nav>
</header>

<section class="hero" role="img" aria-label="Photo of snow-covered wooden chalets and pine trees in an alpine ski village under a blue sky">
  <h2 class="hero-title">For the Best Alpine Accommodation Offers</h2>
</section>

<div class="mode-tabs"><span class="active">I'M SEARCHING</span><span>ALL OFFERS</span></div>

<section class="search-panel">
  <div class="type-tabs">
    <span class="active"><svg width="8" height="7" viewBox="0 0 8 7"><rect x="0" y="3" width="8" height="3" fill="#fff"/><rect x="1" y="1" width="3" height="2" fill="#fff"/></svg>HOTEL</span>
    <span><svg width="7" height="7" viewBox="0 0 7 7"><rect x="1" y="0" width="5" height="7" fill="#fff"/></svg>APARTMENT</span>
    <span><svg width="8" height="7" viewBox="0 0 8 7"><path d="M0 3L4 0 8 3V7H0Z" fill="#fff"/></svg>CHALET</span>
    <span>ALL</span>
  </div>
  <form class="search-form">
    <div class="field">Hotel <span>▾</span></div>
    <div class="field">Enter No. of Rooms <span>▾</span></div>
    <div class="field field-notes">Describe your needs</div>
    <div class="field">Arrival Date <span>▦</span></div>
    <div class="field">Departure Date <span>▾</span></div>
    <div class="field">Number of People <span>▾</span></div>
    <div class="field">Budget <span>EUR</span></div>
    <div class="form-actions"><span class="btn btn-blue">SUBMIT</span><span class="btn btn-blue">SEE ALL OFFERS</span></div>
  </form>
</section>

<section class="welcome">
  <h1>Welcome to <strong>AlpenGlow</strong>Deals</h1>
  <div class="divider"></div>
  <p>Whether you are looking for a cosy room or a full chalet, this is the place to find last minute stays in the mountains. Simply fill in the search form and we will match you with local hosts who have beds free in the next two weeks.</p>
  <p>We work with a friendly team of owners to bring you the best winter deals. You will find hotels, apartments and chalets to suit all budgets.</p>
  <span class="btn btn-purple">READ MORE</span>
</section>

<section class="listings">
  <div class="listings-head"><h2>LATEST LISTINGS</h2><a href="#">View All</a></div>

  <article class="listing">
    <div class="listing-main">
      <div class="listing-photo" role="img" aria-label="Photo of a wooden chalet interior"></div>
      <span class="btn btn-dark">Book</span>
    </div>
    <div class="listing-body">
      <div class="listing-top">
        <div class="listing-title">Chalet Edelweiss</div>
        <div class="listing-actions">
          <span><svg width="7" height="7" viewBox="0 0 10 10"><path d="M5 0l1.5 3.3 3.5.4-2.6 2.4.7 3.5L5 7.8 1.9 9.6l.7-3.5L0 3.7l3.5-.4z" fill="#555"/></svg>FAVOURITES</span>
          <span><svg width="7" height="7" viewBox="0 0 10 10"><rect x="2" y="3" width="6" height="7" fill="#555"/><rect x="1" y="1" width="8" height="1.5" fill="#555"/></svg>DELETE</span>
        </div>
      </div>
      <p class="listing-desc">Bright two bedroom apartment a short walk from the main lifts, with a balcony facing the valley, a fully fitted kitchen and a warm ski room. Free parking and fast wifi for guests staying this week.</p>
      <div class="listing-meta">
        <span><b>Apartment</b> Persons: 4</span><span>Bedrooms: 2</span><span>Price: €450 PW</span>
        <span class="tag"><svg width="6" height="7" viewBox="0 0 6 8"><path d="M3 0a3 3 0 0 1 3 3c0 2-3 5-3 5S0 5 0 3a3 3 0 0 1 3-3z" fill="#555"/></svg>Show Map</span>
        <span class="tag"><svg width="7" height="5" viewBox="0 0 8 6"><rect width="8" height="6" fill="#555"/><path d="M0 0l4 3 4-3" stroke="#fff" fill="none"/></svg>Mail</span>
        <span class="tag"><svg width="6" height="6" viewBox="0 0 8 8"><path d="M1 0h2l1 2-1 1a5 5 0 0 0 2 2l1-1 2 1v2a1 1 0 0 1-1 1A7 7 0 0 1 0 1a1 1 0 0 1 1-1z" fill="#555"/></svg>555-0142</span>
      </div>
    </div>
  </article>

  <article class="listing">
    <div class="listing-main">
      <div class="listing-photo" role="img" aria-label="Photo of a snowy mountain residence"></div>
      <span class="btn btn-dark">Book</span>
    </div>
    <div class="listing-body">
      <div class="listing-top">
        <div class="listing-title">Residence Glacier</div>
        <div class="listing-actions">
          <span><svg width="7" height="7" viewBox="0 0 10 10"><path d="M5 0l1.5 3.3 3.5.4-2.6 2.4.7 3.5L5 7.8 1.9 9.6l.7-3.5L0 3.7l3.5-.4z" fill="#555"/></svg>FAVOURITES</span>
          <span><svg width="7" height="7" viewBox="0 0 10 10"><rect x="2" y="3" width="6" height="7" fill="#555"/><rect x="1" y="1" width="8" height="1.5" fill="#555"/></svg>DELETE</span>
        </div>
      </div>
      <p class="listing-desc">Spacious family apartment in a quiet residence near the nursery slopes, with a log fire, big windows and views to the peaks. Ski lockers on site and a bakery just across the road.</p>
      <div class="listing-meta">
        <span><b>Apartment</b> Persons: 6</span><span>Bedrooms: 3</span><span>Price: €620 PW</span>
        <span class="tag"><svg width="6" height="7" viewBox="0 0 6 8"><path d="M3 0a3 3 0 0 1 3 3c0 2-3 5-3 5S0 5 0 3a3 3 0 0 1 3-3z" fill="#555"/></svg>Show Map</span>
        <span class="tag"><svg width="7" height="5" viewBox="0 0 8 6"><rect width="8" height="6" fill="#555"/><path d="M0 0l4 3 4-3" stroke="#fff" fill="none"/></svg>Mail</span>
        <span class="tag"><svg width="6" height="6" viewBox="0 0 8 8"><path d="M1 0h2l1 2-1 1a5 5 0 0 0 2 2l1-1 2 1v2a1 1 0 0 1-1 1A7 7 0 0 1 0 1a1 1 0 0 1 1-1z" fill="#555"/></svg>555-0142</span>
      </div>
    </div>
  </article>

  <article class="listing">
    <div class="listing-main">
      <div class="listing-photo" role="img" aria-label="Photo of a hotel building in winter"></div>
      <span class="btn btn-dark">Book</span>
    </div>
    <div class="listing-body">
      <div class="listing-top">
        <div class="listing-title">Hotel Bergblick</div>
        <div class="listing-actions">
          <span><svg width="7" height="7" viewBox="0 0 10 10"><path d="M5 0l1.5 3.3 3.5.4-2.6 2.4.7 3.5L5 7.8 1.9 9.6l.7-3.5L0 3.7l3.5-.4z" fill="#555"/></svg>FAVOURITES</span>
          <span><svg width="7" height="7" viewBox="0 0 10 10"><rect x="2" y="3" width="6" height="7" fill="#555"/><rect x="1" y="1" width="8" height="1.5" fill="#555"/></svg>DELETE</span>
        </div>
      </div>
      <p class="listing-desc">Charming double rooms in a family run hotel in the village centre, breakfast included, with a spa, sauna and shuttle to the gondola. Ideal for couples wanting a short winter break.</p>
      <div class="listing-meta">
        <span><b>Hotel</b> Persons: 2</span><span>Bedrooms: 1</span><span>Price: €380 PW</span>
        <span class="tag"><svg width="6" height="7" viewBox="0 0 6 8"><path d="M3 0a3 3 0 0 1 3 3c0 2-3 5-3 5S0 5 0 3a3 3 0 0 1 3-3z" fill="#555"/></svg>Show Map</span>
        <span class="tag"><svg width="7" height="5" viewBox="0 0 8 6"><rect width="8" height="6" fill="#555"/><path d="M0 0l4 3 4-3" stroke="#fff" fill="none"/></svg>Mail</span>
        <span class="tag"><svg width="6" height="6" viewBox="0 0 8 8"><path d="M1 0h2l1 2-1 1a5 5 0 0 0 2 2l1-1 2 1v2a1 1 0 0 1-1 1A7 7 0 0 1 0 1a1 1 0 0 1 1-1z" fill="#555"/></svg>555-0142</span>
      </div>
    </div>
  </article>
</section>

<footer class="site-footer">
  <div class="footer-col login">
    <h3>Advertisers Log In</h3>
    <div class="login-field">Username</div>
    <div class="login-field">Password</div>
    <span class="btn btn-blue">LOG IN</span>
    <div class="social"><span></span><span></span><span></span><span></span></div>
  </div>
  <div class="footer-col testimonials">
    <h3>Client Testimonials</h3>
    <div class="quote-card">We found a lovely apartment two days before our trip and paid far less than expected. The whole booking took minutes and the host was waiting with the keys.</div>
    <div class="quote-author">Anna K., Zurich</div>
  </div>
  <div class="footer-col newsletter">
    <h3>Newsletter Signup</h3>
    <div class="newsletter-box">Join our list to get the latest deals in your inbox and be first to hear about new offers.
      <div class="signup"><div class="field">Email Address</div><span class="btn btn-blue">›</span></div>
    </div>
  </div>
</footer>

<div class="copyright">Copyright © 2015 AlpenGlowDeals.com . All Rights Reserved.</div>

</body>
</html>
```